Letterhead design for business

Looking for an attractive and professional letterhead that uses the logo that is attached below.

Target Market(s)

Potential bankruptcy clients.

Industry/Entity Type

Legal

Colors

Designer to choose colors to be used in the design.

Requirements
Must have
• Address for locations, phone number, and website address.
• Addresses are on website ferncoveadvice.example. Use following phone number (for tracking purposes): 555-013-8274

```html
<!DOCTYPE html>
<html lang="en">
<head>
<meta charset="utf-8">
<title>Ferncove Advice Law Group – Letterhead</title>
<link href="https://fonts.googleapis.com/css2?family=Lato:wght@300;400&family=Roboto:wght@400;500&display=swap" rel="stylesheet">
<style>
  :root {
    --backdrop: #e6e4e1;
    --paper: #ffffff;
    --brand-green: #80bf87;
    --brand-dark: #424242;
    --ink: #3d3d3d;
    --ink-soft: #555555;
    --on-green: #ffffff;
  }
  html, body {
    margin: 0;
    padding: 0;
    width: 1200px;
    height: 1120px;
    overflow: hidden;
    background: var(--backdrop);
  }
  .letterhead {
    position: absolute;
    left: 190px;
    top: 20px;
    width: 819px;
    height: 1080px;
    background: var(--paper);
    box-shadow: 0 4px 14px rgba(0,0,0,0.25);
    font-family: 'Lato', sans-serif;
    color: var(--ink);
    overflow: hidden;
  }
  .brand {
    position: absolute;
    left: 66px;
    top: 72px;
    display: flex;
    align-items: center;
    gap: 14px;
  }
  .brand-dot {
    width: 64px;
    height: 64px;
    border-radius: 50%;
    background: var(--brand-green);
  }
  .brand-rule {
    width: 2px;
    height: 74px;
    background: var(--brand-green);
  }
  .brand-text { line-height: 1; }
  .brand-name {
    font-family: 'Lato', sans-serif;
    font-weight: 400;
    font-size: 27px;
    color: var(--brand-green);
    letter-spacing: -0.3px;
  }
  .brand-sub {
    font-family: 'Roboto', sans-serif;
    font-size: 11px;
    letter-spacing: 2.6px;
    color: var(--ink);
    margin-top: 6px;
    padding-left: 28px;
  }
  .brand-tagline {
    font-family: 'Roboto', sans-serif;
    font-size: 8.5px;
    color: var(--brand-green);
    margin-top: 4px;
    padding-left: 44px;
  }
  .date {
    position: absolute;
    left: 66px;
    top: 246px;
    font-size: 16px;
    font-weight: 400;
  }
  .recipient {
    position: absolute;
    left: 66px;
    top: 292px;
    font-size: 15px;
    font-weight: 300;
    line-height: 19px;
  }
  .recipient .salutation { font-weight: 400; font-size: 16px; }
  .body-copy {
    position: absolute;
    left: 66px;
    top: 413px;
    width: 672px;
    font-size: 15px;
    font-weight: 300;
    line-height: 23.1px;
    text-align: justify;
    hyphens: auto;
  }
  .body-copy p { margin: 0 0 22px; }
  .signature {
    position: absolute;
    left: 66px;
    top: 848px;
  }
  .signature .name { font-size: 20px; font-weight: 400; }
  .signature .role { font-size: 14px; font-weight: 300; color: var(--ink-soft); margin-top: 8px; }
  .footer {
    position: absolute;
    left: 0;
    bottom: 0;
    width: 819px;
    height: 118px;
  }
  .footer svg { position: absolute; left: 0; top: 0; }
  .contact {
    position: absolute;
    left: 70px;
    top: 12px;
    font-family: 'Roboto', sans-serif;
    font-weight: 500;
    font-size: 12px;
    color: var(--on-green);
    line-height: 15px;
  }
  .contact .address { margin-bottom: 9px; }
  .contact .line { display: flex; align-items: center; gap: 6px; height: 16.5px; }
  .contact svg { position: static; }
</style>
</head>
<body>
<main class="letterhead">
  <header class="brand">
    <div class="brand-dot"></div>
    <div class="brand-rule"></div>
    <div class="brand-text">
      <div class="brand-name">Ferncove Advice</div>
      <div class="brand-sub">LAW GROUP</div>
      <div class="brand-tagline">by Attorney M. Halvorsen</div>
    </div>
  </header>

  <div class="date">May 10, 2018</div>

  <div class="recipient">
    <div class="salutation">Dear Mr. Tarrant</div>
    <div>demo street,</div>
    <div>demo placeP.O.</div>
    <div>Box 000, 555 Avenue</div>
  </div>

  <section class="body-copy">
    <p>Lorem ipsum dolor sit amet, consectetur adipiscing elit. Donec orci purus, luctus vitae dignissim eu, iaculis sed purus. Vivamus faucibus, ipsum nec aliquet viverra, leo mauris condimentum ligula, sit amet sagittis enim ligula quis arcu. Nam egestas tortor id nisi porttitor mattis. In tortor ante, ultricies in suscipit a, tempus non massa. Vivamus et auctor mi. Fusce vel massa nulla. Phasellus nec eros mauris, et scelerisque orci. Donec malesuada orci vitae nulla accumsan porta a id massa. Quisque accumsan iaculis magna sit amet fringilla. Maecenas consequat, magna eget tincidunt semper, odio nibh rutrum mi, id feugiat ante nisi eu risus. Vestibulum nunc orci, rhoncus a placerat in, ultricies in mi. Cras mattis varius eros, vel fringilla nisi suscipit eget.</p>
    <p>Quisque scelerisque sagittis nulla at porttitor. Mauris a justo et tellus interdum tristique. Sed id augue vitae urna euismod commodo aliquet a quam. Pellentesque arcu velit, cursus et malesuada ut, consequat et diam. Nullam erat sem, rhoncus id ullamcorper vitae, rhoncus et arcu. In ultricies ultricies nulla, ut rutrum nisi iaculis at. Donec eu magna a metus ornare faucibus. Fusce aliquet faucibus ultricies. Morbi semper, est id tincidunt gravida, sem arcu adipiscing lacus, ac bibendum nulla leo eu purus. Quisque nec diam sed risus consectetur a ccumsan quis quis nibh. Vestibulum id purus <span style="font-size:18px">lorem.</span></p>
  </section>

  <div class="signature">
    <div class="name">John Doe</div>
    <div class="role">Co-Founder &amp; CEO</div>
  </div>

  <footer class="footer">
    <svg width="819" height="118" viewBox="0 0 819 118">
      <path d="M0 0 H246 Q272 0 290 26 L353 118 H0 Z" fill="var(--brand-green)"/>
      <path d="M323 62 H819 V118 H361 Z" fill="var(--brand-dark)"/>
    </svg>
    <div class="contact">
      <div class="address">Address, demo street 088<br>P.O. Box 000, 555 Avenue</div>
      <div class="line">
        <svg width="10" height="10" viewBox="0 0 24 24"><path fill="#fff" d="M6.6 10.8a15.1 15.1 0 0 0 6.6 6.6l2.2-2.2a1 1 0 0 1 1-.25 11.4 11.4 0 0 0 3.6.6 1 1 0 0 1 1 1V20a1 1 0 0 1-1 1A17 17 0 0 1 3 4a1 1 0 0 1 1-1h3.5a1 1 0 0 1 1 1c0 1.25.2 2.45.6 3.6a1 1 0 0 1-.25 1z"/></svg>
        <span>555-013-8274</span>
      </div>
      <div class="line">
        <svg width="10" height="8" viewBox="0 0 20 14"><rect x="0" y="0" width="20" height="14" rx="1.5" fill="#fff"/><path d="M1 1 L10 8 L19 1" stroke="#80bf87" stroke-width="1.6" fill="none"/></svg>
        <span>info@ferncoveadvice.example</span>
      </div>
      <div class="line">
        <svg width="10" height="10" viewBox="0 0 20 20"><circle cx="10" cy="10" r="8.5" fill="none" stroke="#fff" stroke-width="1.6"/><ellipse cx="10" cy="10" rx="3.5" ry="8.5" fill="none" stroke="#fff" stroke-width="1.4"/><line x1="1.5" y1="10" x2="18.5" y2="10" stroke="#fff" stroke-width="1.4"/></svg>
        <span>www.ferncoveadvice.example</span>
      </div>
    </div>
  </footer>
</main>
</body>
</html>
```